Poster to advertise new mind coaching clinic

Create a single sided A4 colour poster using the text provided. Suggested image provided. You may want to suggest an alternative however images need to appeal to both male and female sports people.

Text:
One-to-one mind coaching
For recreational and competitive sports people
Learn the mental tools and techniques used by the top sports people to fulfil your potential

 Create well-formed and achievable goals
 Overcome limiting beliefs
 Accelerate mastery through modelling your heroes
 Learn how to use mental rehearsal to increase your chances of success
 Smash through belief ceilings
 Get into the zone to bring your ‘best game’ more often
Thursdays in central Twyford
5-8pm
For more information contact:
stellvanementoring@quorvexmail.com
Tel: 07700 900482
www.stellvane-mind.co.uk

sports people

Clinic

• All the content provided. Contact details.

```html
<!DOCTYPE html>
<html lang="en">
<head>
<meta charset="utf-8">
<title>Stellvane – One-to-one mind coaching</title>
<link href="https://fonts.googleapis.com/css2?family=Oswald:wght@300;400;500&family=Montserrat:wght@600;700&family=Arimo:wght@400;700&display=swap" rel="stylesheet">
<style>
  :root {
    --navy: #0a1e6e;
    --royal: #0a55b4;
    --deep: #06206f;
    --sky: #23bdee;
    --cyan: #3fd0f5;
    --link-blue: #1a5fae;
    --tel-blue: #29b3e8;
    --ink: #111111;
    --white: #ffffff;
  }
  * { margin: 0; padding: 0; box-sizing: border-box; }
  html, body { width: 848px; height: 1200px; overflow: hidden; background: var(--white); }
  .poster { position: relative; width: 848px; height: 1200px; overflow: hidden; background: var(--white); }
  .backdrop { position: absolute; inset: 0; }

  .brand {
    position: absolute; top: 62px; left: 0; width: 848px;
    display: flex; justify-content: center; align-items: center; gap: 16px;
  }
  .brand-dot { width: 40px; height: 40px; border-radius: 50%; background: var(--sky); }
  .brand-name {
    font-family: "Montserrat", sans-serif; font-weight: 700;
    font-size: 64px; color: var(--ink); letter-spacing: -1px;
  }

  .headline {
    position: absolute; left: 220px; top: 238px;
    transform-origin: 0 0; transform: scaleX(0.83);
    font-family: "Oswald", sans-serif; font-weight: 500;
    font-size: 106px; line-height: 82px; color: var(--white); white-space: nowrap;
  }

  .pitch {
    position: absolute; left: 594px; top: 548px; width: 226px;
    font-family: "Montserrat", sans-serif; font-weight: 600;
    font-size: 26.5px; line-height: 35.5px; color: var(--white);
  }

  .audience {
    position: absolute; left: 48px; top: 588px;
    transform-origin: 0 0; transform: rotate(31deg) scaleX(0.88);
    font-family: "Oswald", sans-serif; font-weight: 500;
    font-size: 42px; color: var(--navy); white-space: nowrap;
  }

  .benefits {
    position: absolute; left: 40px; top: 822px; list-style: none;
    font-family: "Arimo", sans-serif; font-weight: 700;
    font-size: 19px; line-height: 27px; color: var(--ink);
  }
  .benefits li { position: relative; padding-left: 26px; }
  .benefits svg { position: absolute; left: 0; top: 9px; }

  .session { position: absolute; left: 0; top: 1112px; width: 330px; height: 58px; }
  .session-text {
    position: absolute; left: 53px; top: 1123px;
    transform-origin: 0 0; transform: scaleX(0.9);
    font-family: "Oswald", sans-serif; font-weight: 400;
    font-size: 21px; color: var(--white); white-space: nowrap;
  }

  .contact {
    position: absolute; left: 392px; top: 1100px; width: 436px;
    text-align: center; font-family: "Arimo", sans-serif;
  }
  .contact-lead { font-size: 11.5px; color: var(--ink); }
  .contact-line { font-size: 15px; color: var(--ink); margin-top: 4px; white-space: nowrap; }
  .contact-tel { color: var(--tel-blue); margin-left: 6px; }
  .contact-web { font-size: 21px; font-weight: 700; color: var(--link-blue); margin-top: 4px; }
</style>
</head>
<body>
<main class="poster">
  <svg class="backdrop" width="848" height="1200" viewBox="0 0 848 1200">
    <defs>
      <linearGradient id="blue-field" x1="0" y1="0" x2="1" y2="1">
        <stop offset="0" stop-color="#1aa6e6"/>
        <stop offset="0.45" stop-color="#0a55b4"/>
        <stop offset="1" stop-color="#06206f"/>
      </linearGradient>
      <linearGradient id="metal-band" x1="0" y1="0" x2="1" y2="0">
        <stop offset="0" stop-color="#ffffff"/>
        <stop offset="0.45" stop-color="#c8c8c8"/>
        <stop offset="0.75" stop-color="#e4e4e4"/>
        <stop offset="1" stop-color="#6d6d6d"/>
      </linearGradient>
      <radialGradient id="athlete-glow" cx="0.5" cy="0.55" r="0.5">
        <stop offset="0" stop-color="#5a7fc0"/>
        <stop offset="0.6" stop-color="#2a6bc4" stop-opacity="0.7"/>
        <stop offset="1" stop-color="#0a55b4" stop-opacity="0"/>
      </radialGradient>
    </defs>
    <polygon class="metal-band" points="0,206 848,168 848,220 0,210" fill="url(#metal-band)"/>
    <polygon class="blue-field" points="0,220 848,220 848,952 0,532" fill="url(#blue-field)"/>
    <rect class="athlete-photo" role="img" aria-label="Sprinter crossing the finish line with arms spread wide in celebration"
          x="150" y="330" width="660" height="490" fill="url(#athlete-glow)"/>
    <polygon class="ribbon" points="0,532 848,952 848,977 704,980 718,1080 0,648" fill="var(--sky)"/>
  </svg>

  <div class="brand">
    <span class="brand-dot"></span>
    <span class="brand-name">Stellvane</span>
  </div>

  <h1 class="headline">One-to-one<br>mind coaching</h1>

  <p class="pitch">Learn the mental tools and techniques used by the top sports people to fulfil your potential</p>

  <p class="audience">For recreational and competitive sports people</p>

  <ul class="benefits">
    <li><svg width="12" height="10" viewBox="0 0 12 10"><path d="M1 5 L4.5 8.5 L11 1" fill="none" stroke="var(--tel-blue)" stroke-width="2"/></svg>Create well-formed and<br>achievable goals</li>
    <li><svg width="12" height="10" viewBox="0 0 12 10"><path d="M1 5 L4.5 8.5 L11 1" fill="none" stroke="var(--tel-blue)" stroke-width="2"/></svg>Overcome limiting beliefs</li>
    <li><svg width="12" height="10" viewBox="0 0 12 10"><path d="M1 5 L4.5 8.5 L11 1" fill="none" stroke="var(--tel-blue)" stroke-width="2"/></svg>Accelerate mastery through<br>modelling your heroes</li>
    <li><svg width="12" height="10" viewBox="0 0 12 10"><path d="M1 5 L4.5 8.5 L11 1" fill="none" stroke="var(--tel-blue)" stroke-width="2"/></svg>Learn how to use mental rehearsal to<br>increase your chances of success</li>
    <li><svg width="12" height="10" viewBox="0 0 12 10"><path d="M1 5 L4.5 8.5 L11 1" fill="none" stroke="var(--tel-blue)" stroke-width="2"/></svg>Smash through belief ceilings</li>
    <li><svg width="12" height="10" viewBox="0 0 12 10"><path d="M1 5 L4.5 8.5 L11 1" fill="none" stroke="var(--tel-blue)" stroke-width="2"/></svg>Get into the zone to bring your ‘best game’<br>more often</li>
  </ul>

  <svg class="session" width="330" height="58" viewBox="0 0 330 58">
    <polygon points="0,0 330,0 312,58 0,58" fill="var(--cyan)"/>
    <polygon points="0,0 322,0 304,54 0,54" fill="var(--royal)"/>
  </svg>
  <p class="session-text">Thursdays in central Twyford 5-8pm</p>

  <div class="contact">
    <p class="contact-lead">For more information contact:</p>
    <p class="contact-line">stellvanementoring@quorvexmail.com<span class="contact-tel">Tel: 07700 900482</span></p>
    <p class="contact-web">www.stellvane-mind.co.uk</p>
  </div>
</main>
</body>
</html>
```